Morvane Locks price sheet/brochure

So I'm looking to create a pricing sheet/brochure for my hair company. The company name is "Morvane Locks" and we specialize in providing Peruvian, Brazilian and Indian weave hair. I created a logo some time ago that I'd like to use if possible. If not, I'll need to create a logo as well!

8.5 x 11....not sure how many pages are needed to properly display all pricing, but I'd like the pricing to be at a size that makes it easy for the client to read. Open A-3

Target Market(s)

Hair stylist as well as their clients. Looking to establish business in Africa as well!

Industry/Entity Type

Hair And Beauty

Font styles to use
Serif

Colors
e34298

Requirements
Must have
• Price sheet/brochure must be easy to read and give potential client all the pertinent information needed regarding our hair! Also want the brochure to present style and pride in the excellent quality hair the "Morvane Locks"! 😀
• Morvane Locks
• Base price for all hair textures. Pricing will increase depending on wave pattern.
• Peruvian & Brazilian Virgin Hair
• 4 bundle deals
• 10, 12, 14, 16 - $405
• 12, 14, 16, 18 - $434
• 14, 16, 18, 20 - $467
• 16, 18, 20, 22 - $504
• 18, 20, 22, 24 - $539
• 20, 22, 24, 26 - $576
• 22, 24, 26, 28 - $621
• 24, 26, 28, 30 - $660
• 26, 28, 30, 32 - $693
• 28, 30, 32, 34 - $728
• 30, 32, 34, 36 - $760
• 32, 34, 36, 38 - $799
• 3 bundle deals
• 10, 12, 14 - $281
• 12, 14, 16 - $333
• 14, 16, 18 - $358
• 16, 18, 20 - $385
• 18, 20, 22 - $410
• 20, 22, 24 - $432
• 22, 24, 26 - $471
• 24, 26, 28 - $500
• 26, 28, 30 - $533
• 28, 30, 32 - $560
• 30, 32, 34 - $589
• 32, 34, 36 - $608
• 34, 36, 38 - $635
• 2 Bundles
• 2 Bundles 10 - $203
• 2 Bundles 12 - $235
• 2 Bundles 14 - $251
• 2 Bundles 16 - $272
• 2 Bundles 18 - $285
• 2 Bundles 20 - $302
• 2 Bundles 22 - $346
• 2 Bundles 24 - $345
• 2 Bundles 26 - $357
• 2 Bundles 28 - $384
• 2 Bundles 30 - $418
• 2 Bundles 32 - $429
• 2 Bundles 34 - $440
• 2 Bundles 36 - $476
• 2 Bundles 38 - $502
• 1 Bundle
• 1 Bundle 10 - $97
• 1 Bundle 12 - $110
• 1 Bundle 14 - $116
• 1 Bundle 16 - $126
• 1 Bundle 18 - $134
• 1 Bundle 20 - $141
• 1 Bundle 22 - $154
• 1 Bundle 24 - $167
• 1 Bundle 26 - $172
• 1 Bundle 28 - $185
• 1 Bundle 30 - $192
• 1 Bundle 32 - $197
• 1 Bundle 34 - $205
• 1 Bundle 36 - $215
• 1 Bundle 38 - $230
• -----------------------------------------------------------------------------
• Indian Virgin Hair
• 4 bundle deals
• 10, 12, 14, 16 - $293
• 12, 14, 16, 18 - $314
• 14, 16, 18, 20 - $325
• 16, 18, 20, 22 - $348
• 18, 20, 22, 24 - $367
• 20, 22, 24, 26 - $386
• 22, 24, 26, 28 - $407
• 24, 26, 28, 30 - $425
• 26, 28, 30, 32 - $444
• 28, 30, 32, 34 - $461
• 30, 32, 34, 36 - $477
• 32, 34, 36, 38 - $495
• 3 bundle deals
• 10, 12, 14 - $223
• 12, 14, 16 - $239
• 14, 16, 18 - $252
• 16, 18, 20 - $264
• 18, 20, 22 - $278
• 20, 22, 24 - $293
• 22, 24, 26 - $308
• 24, 26, 28 - $322
• 26, 28, 30 - $337
• 28, 30, 32 - $350
• 30, 32, 34 - $262
• 32, 34, 36 - $375
• 34, 36, 38 - $390
• 2 Bundles
• 2 Bundles 10 - $74
• 2 Bundles 12 - $90
• 2 Bundles 14 - $98
• 2 Bundles 16 - $107
• 2 Bundles 18 - $115
• 2 Bundles 20 - $123
• 2 Bundles 22 - $135
• 2 Bundles 24 - $143
• 2 Bundles 26 - $154
• 2 Bundles 28 - $164
• 2 Bundles 30 - $172
• 2 Bundles 32 - $180
• 2 Bundles 34 - $189
• 2 Bundles 36 - $197
• 2 Bundles 38 - $207
• 1 Bundle
• 1 Bundle 10 - $80
• 1 Bundle 12 - $88
• 1 Bundle 14 - $93
• 1 Bundle 16 - $98
• 1 Bundle 18 - $102
• 1 Bundle 20 - $109
• 1 Bundle 22 - $115
• 1 Bundle 24 - $122
• 1 Bundle 26 - $130
• 1 Bundle 28 - $137
• 1 Bundle 30 - $144
• 1 Bundle 32 - $156
• 1 Bundle 34 - $163
• 1 Bundle 36 - $175
• 1 Bundle 38 - $190
• Hair Care
• It's very important to take good care of your hair to keep using long time, below are some brief introduction
• IMPORTANT: Treat 100% human hair extensions gently.
• 1. Wash and condition hair regularly, at maximum of 3 times a week. This will keep the moisture in from shampooing while at the same time not drying them out from over shampooing.
• 2. Combing hair gently before washing. Do not rub or twist hair.
• 3. Add mild shampoo to cool water or warm water about 35℃ (Please do not use hot water) and swish hair till clean. Rinse thoroughly.
• 4. Blot out excess water with towel and allow hair to dry naturally. Do not expose to sun
• 5. Comb curly hair gently with your fingers from end to top. Do not brush
• 6. Hair may be tangled if general care directions are not followed properly.
• Important Note:
• Brush the end of hair first, then the middle, and the top at last. DO NOT brush directly from the top and pull hard, it will break the hair. Regular care will keep the hair in good condition and avoid tangle problem, improper dyeing or other chemical process will damage the hair and cause tangle and shedding problem. Please wash the hair with warm water before proceeding dyeing.
• Details of Hair Extension Maintenance Tips
• Straight Hair:
• Maintenance
• • Shampoo at least once a week.
• • Use a shampoo no higher than pH 7.
• • Dilute one ounce of shampoo in a bowl or jug with a pint of warm water.
• • Sponge the shampoo into the hair.
• • Do not massage.
• • Rinse thoroughly.
• • Apply conditioner and comb hair, starting with the ends working your way up to your scalp.
• • Rinse thoroughly.
• • Let air-dry.
• Daily
• • Brush or comb through to style.
• • Use styling aids, such as mouse, gel, and hairspray in moderation (preferably alcohol free products).
• Sleep
• • Before going to bed, braid your hair into one loose large braid at the back of the neck.
• • After waking up, undo braid and comb through beginning at the ends and working your way up to roots.
• Natural Body Wave Hair
• Maintenance
• • Do not massage.
• • Rinse thoroughly.
• • Rinse thoroughly.
• • Let air-dry.
• • Style as desired.
• • For extra wave, hair can be set in rollers.
• Daily
• Sleep
• • After waking up, undo braid.
• • Dampen hair with a water bottle.
• • Comb through beginning at the ends and working your way up to roots.
• • Let hair air-dry.
• • Style as desired.
• For extra wave, hair can be set in rollers.
• Permed Curly and Natural Curly Hair
• Maintenance
• • Do not use oil products on permed hair, it can cause matting.
• • Do not brush or comb hair when dry, it will cause frizz and the ends may tangle.
• • Do not massage.
• • Rinse thoroughly.
• • Rinse thoroughly.
• • Scrunch up hair gently to reform curl.
• • Let air-dry.
• • Style as desired.
• Daily
• Sleep
• • Let hair air-dry.
• • Style as desired.
• Specific Conditions
• Static:
• • In colder months, you may experience some static. The best way to deal with this is to dampen your hands with water, and rub hand together so they are warm. Run the palms of your hands over your hair, without actually touching your hair. This process should help control the static.
• Swimming:
• It is not recommended that you swim with extension hair. However if you do the following precautions are recommended.
• • Never wear a swimming cap or anything that covers your hair, the friction may cause matting.
• • Before swimming comb out tangles.
• • Braid hair into one braid at back of neck.
• • Try to keep head above water.
• • Do not swim under water.
• • No diving.
• • After swimming keep head out of shower.
• • Immediately after showering undo braid, comb hair and let air-dry.
• • Follow with appropriate shampooing and conditioning as needed.
• Sauna:
• • The water of the sauna will penetrate the hair and wet it.
• • Do not wrap hair in towel, which will compress it.
• • After sauna keep head out of shower.
• Sunbathing:
• • After sunbathing do not unbraid until hair has cooled down.
• • After hair cools, undo braid, comb hair.
• Miscellaneous Tips:
• • Although the extension hair is real, it is not receiving nutrients from the scalp like your own hair. Heat is your hair extensions biggest enemy. The more you use on it, the shorter the life span of your hair. We cannot guarantee that the hair will remain silky if you use the blow dry, flat iron, or curling iron often.
• • When you sleep, we highly recommend that you braid, wrap or ponytail your hair together to prevent tangling. This will save time that would be spent untangling the hair the next morning.
• • When washing the hair, always wash it going in a downward motion. Use your fingers in a horizontal motion between wefts to clean your scalp. When rinsing, do the same to be sure that all the shampoo and conditioner residues are washed out.
• Sent from my Vorna
Nice to have
• Ditto....tried to upload logo but it was to big. Please advise!
Should not have
• Ditto....

```html
<!DOCTYPE html>
<html lang="en">
<head>
<meta charset="utf-8">
<title>Morvane Locks – Hair Care &amp; Straight Hair</title>
<link rel="stylesheet" href="https://fonts.googleapis.com/css2?family=Oswald:wght@300;400;500&display=swap">
<style>
  :root {
    --cream: #eeeedd;
    --lime: #b3d23a;
    --teal: #37b8a3;
    --teal-frame: #5cc0ae;
    --ink: #545454;
    --ink-strong: #4a4a4a;
    --white: #ffffff;
  }
  * { margin: 0; padding: 0; box-sizing: border-box; }
  html, body { width: 1200px; height: 848px; overflow: hidden; background: var(--cream); }
  .sheet {
    position: relative; width: 1200px; height: 848px; overflow: hidden;
    background: var(--cream);
    font-family: "Oswald", sans-serif; font-weight: 300; color: var(--ink);
  }
  .panel-outer { position: absolute; top: 12px; height: 824px; border: 6px solid var(--lime); }
  .panel-inner { position: absolute; top: 26px; height: 796px; border: 8px solid var(--teal-frame); }
  .left-outer { left: 14px; width: 570px; }
  .left-inner { left: 30px; width: 540px; }
  .right-outer { left: 614px; width: 572px; }
  .right-inner { left: 630px; width: 540px; }

  .rule { position: absolute; top: 50px; height: 1px; background: var(--ink-strong); }
  .banner {
    position: absolute; top: 52px; height: 50px;
    display: flex; align-items: center; justify-content: center;
    clip-path: polygon(0 0, 100% 0, 100% 70%, calc(100% - 15px) 100%, 15px 100%, 0 70%);
    color: var(--white); font-weight: 400; font-size: 37px; letter-spacing: -0.5px;
    text-shadow: 1px 1px 2px rgba(0,0,0,0.35);
  }
  .banner-care { left: 48px; width: 503px; background: var(--teal); }
  .banner-straight { left: 653px; width: 502px; background: var(--lime); }
  .rule-care { left: 48px; width: 503px; }
  .rule-straight { left: 653px; width: 502px; }

  .intro { position: absolute; left: 49px; top: 118px; font-size: 17px; line-height: 22.5px; }
  .important {
    position: absolute; left: 48px; width: 503px; top: 186px; text-align: center;
    font-size: 20px; font-weight: 500; color: var(--ink-strong);
  }
  .important .accent { color: var(--teal); }
  .care-step { position: absolute; left: 50px; font-size: 17.4px; line-height: 22.8px; }
  .care-step .num { padding-right: 6px; }
  .note-heading {
    position: absolute; left: 48px; width: 503px; top: 608px; text-align: center;
    font-size: 20px; font-weight: 500; color: var(--teal);
  }
  .note-body {
    position: absolute; left: 40px; width: 520px; top: 650px; text-align: center;
    font-size: 17.4px; line-height: 22.7px;
  }

  .subtitle {
    position: absolute; left: 653px; width: 502px; top: 114px; text-align: center;
    font-size: 19px; font-weight: 500; color: var(--ink-strong);
  }
  .section-title { position: absolute; left: 653px; font-size: 20px; font-weight: 500; color: var(--teal); }
  .tips { position: absolute; left: 654px; list-style: none; font-size: 17.4px; line-height: 25.6px; }
  .tips li { padding-left: 12px; text-indent: -12px; }
  .tips li::before { content: "•"; display: inline-block; width: 12px; text-indent: 0; }
  .tips-wide li { white-space: nowrap; }

  .photo { position: absolute; left: 950px; top: 170px; width: 260px; height: 340px; }
</style>
</head>
<body>
<main class="sheet">
  <section class="hair-care">
    <div class="panel-outer left-outer"></div>
    <div class="panel-inner left-inner"></div>
    <div class="rule rule-care"></div>
    <h1 class="banner banner-care">HAIR CARE</h1>
    <p class="intro">It's very important to take good care of your hair to keep using long time,<br>below are some brief introduction:</p>
    <p class="important"><span class="accent">IMPORTANT:</span> Treat 100% human hair extensions gently.</p>

    <p class="care-step" style="top:229px"><span class="num">1.</span> Wash and condition hair regularly, at maximum of 3 times a week.<br>This will keep the moisture in from shampooing while at the same<br>time not drying them out from over shampooing.</p>
    <p class="care-step" style="top:309px"><span class="num">2.</span> Combing hair gently before washing. Do not rub or twist hair.</p>
    <p class="care-step" style="top:343px"><span class="num">3.</span> Add mild shampoo to cool water or warm water about 35˚C,<br>(please do not use hot water) and swish hair till clean.<br>Rinse thoroughly.</p>
    <p class="care-step" style="top:423px"><span class="num">4.</span> Blot out excess water with towel and allow hair to dry naturally.<br>Do not expose to sun.</p>
    <p class="care-step" style="top:480px"><span class="num">5.</span> Comb curly hair gently with your fingers from end to top.<br>Do not brush.</p>
    <p class="care-step" style="top:537px"><span class="num">6.</span> Hair may be tangled if general care directions are not followed<br>properly.</p>

    <h2 class="note-heading">IMPORTANT NOTE:</h2>
    <p class="note-body">Brush the end of hair first, then the middle, and the top at last.<br>DO NOT brush directly from the top and pull hard, it will break the hair.<br>Regular care will keep the hair in good condition and avoid tangle<br>problem, improper dyeing or other chemical process will<br>damage the hair and cause tangle and shedding problem.<br>Please wash the hair with warm water before proceeding dyeing.</p>
  </section>

  <section class="straight-hair">
    <div class="panel-outer right-outer"></div>
    <div class="panel-inner right-inner"></div>
    <div class="rule rule-straight"></div>
    <h1 class="banner banner-straight">STRAIGHT HAIR</h1>
    <h2 class="subtitle">Details of Hair Extension Maintenance Tips</h2>

    <h3 class="section-title" style="top:186px">MAINTENANCE</h3>
    <ul class="tips tips-wide" style="top:228px">
      <li>Shampoo at least once a week.</li>
      <li>Use a shampoo no higher than pH 7.</li>
      <li>Dilute one ounce of shampoo in a bowl<br>or jug with a pint of warm water.</li>
      <li>Sponge the shampoo into the hair.</li>
      <li>Do not massage.</li>
      <li>Rinse thoroughly.</li>
      <li>Apply conditioner and comb hair, starting<br>with the ends working your way up to your scalp.</li>
      <li>Rinse thoroughly.</li>
      <li>Let air-dry.</li>
    </ul>

    <h3 class="section-title" style="top:528px">DAILY</h3>
    <ul class="tips tips-wide" style="top:557px">
      <li>Brush or comb through to style.</li>
      <li>Use styling aids, such as mouse, gel, and hairspray in moderation<br>(preferably alcohol free products).</li>
    </ul>

    <h3 class="section-title" style="top:652px">SLEEP</h3>
    <ul class="tips tips-wide" style="top:685px">
      <li>Before going to bed, braid your hair into one loose large braid<br>at the back of the neck.</li>
      <li>After waking up, undo braid and comb through beginning<br>at the ends and working your way up to roots.</li>
    </ul>

    <svg class="photo" viewBox="0 0 260 340" role="img" aria-label="Photo of a model with long, straight auburn hair extensions">
      <defs>
        <linearGradient id="hairTone" x1="0" y1="0" x2="0.3" y2="1">
          <stop offset="0" stop-color="#f4f1ee"/>
          <stop offset="0.3" stop-color="#a2462a"/>
          <stop offset="0.7" stop-color="#7a2e1c"/>
          <stop offset="1" stop-color="#3d1e17"/>
        </linearGradient>
      </defs>
      <polygon points="12,18 262,6 262,302 94,332" fill="var(--teal)"/>
      <polygon points="24,27 262,16 262,292 101,320" fill="url(#hairTone)"/>
    </svg>
  </section>
</main>
</body>
</html>
```